Business card for my new company (Accounting firm)

I need a business card for my new business Corvane Advisory and Ledger SA. Our services are accounting, tax, audit and financial management. Our customers are small companies, start-ups and new companies. The final design has to show financial security, trust and growth. Please find our logo attached to the business card. Text for the business card: Corvane Advisory and Ledger SA Tomas da Varela Director and Founder Certified Accountant Tel. 022 418 27 35 tv@corvaneconseil.ch www.corvaneconseil.ch Rue des Vergers-Bleus 14 1201 Geneva
Target Market(s)
Our customers are small companies, start-ups and new companies.
Industry/Entity Type
Finance And Accounting
Contact Information for Business Card
Corvane Conseil et Registre SA
Tomas da Varela
Directeur et Fondateur
Expert-comptable diplômé
Tél. 022 418 27 35
tv@corvaneconseil.ch
www.corvaneconseil.ch
Rue des Vergers-Bleus 14
1201 Genève

```html
<!DOCTYPE html>
<html lang="fr">
<head>
<meta charset="utf-8">
<title>Corvane Conseil et Registre SA — Carte de visite</title>
<link rel="stylesheet" href="https://fonts.googleapis.com/css2?family=Roboto:wght@400;500;700&display=swap">
<style>
  :root {
    --backdrop: #2b2b2d;
    --card: #ffffff;
    --edge: #1a6496;
    --ink: #3a3a3c;
    --ink-soft: #58585b;
    --blue-light: #33aee2;
    --blue-mid: #2187c6;
    --blue-deep: #1a6496;
  }
  html, body {
    margin: 0;
    padding: 0;
    width: 1200px;
    height: 960px;
    overflow: hidden;
    background: var(--backdrop);
    font-family: "Roboto", Arial, sans-serif;
  }
  .stage {
    position: relative;
    width: 1200px;
    height: 960px;
    display: flex;
    align-items: center;
    justify-content: center;
    gap: 48px;
  }
  .card {
    position: relative;
    width: 530px;
    height: 342px;
    background: var(--card);
    border-bottom: 4px solid var(--edge);
    box-sizing: border-box;
    overflow: hidden;
  }

  /* Back side */
  .card--back {
    display: flex;
    flex-direction: column;
    align-items: center;
    justify-content: center;
  }
  .brand {
    display: flex;
    align-items: center;
    gap: 12px;
  }
  .brand__mark {
    width: 22px;
    height: 22px;
    background: var(--blue-mid);
    flex: none;
  }
  .brand__name {
    color: var(--ink);
    font-weight: 500;
    text-transform: uppercase;
    line-height: 1.05;
  }
  .brand__name span { display: block; }
  .card--back .brand__name { font-size: 34px; letter-spacing: 5px; }
  .card--back .brand__name span + span { font-size: 13px; letter-spacing: 3.4px; margin-top: 4px; }
  .card--back .web {
    margin-top: 26px;
    font-size: 15px;
    letter-spacing: 4px;
    color: var(--ink-soft);
  }

  /* Front side */
  .card--front { display: flex; }
  .front__info {
    padding: 40px 0 0 40px;
    width: 300px;
  }
  .card--front .brand__name { font-size: 32px; letter-spacing: 5px; }
  .card--front .brand__name span + span { font-size: 12px; letter-spacing: 3px; margin-top: 4px; }
  .person { margin-top: 30px; }
  .person__name {
    color: var(--blue-light);
    font-weight: 700;
    font-size: 22px;
    margin: 0;
  }
  .person__role {
    color: var(--ink);
    font-size: 15px;
    line-height: 1.3;
    margin: 2px 0 0;
  }
  .address {
    margin-top: 14px;
    font-style: normal;
    color: var(--ink-soft);
    font-size: 15px;
    line-height: 1.3;
  }
  .contacts {
    list-style: none;
    padding: 0;
    margin: 12px 0 0;
    color: var(--ink);
    font-size: 15px;
    line-height: 1.45;
  }
  .contacts li { display: flex; align-items: center; gap: 10px; }
  .contacts svg { width: 14px; height: 14px; fill: var(--blue-light); flex: none; }
  .front__accent {
    position: absolute;
    right: 52px;
    top: 72px;
    width: 190px;
    height: 190px;
    background: var(--blue-mid);
  }
</style>
</head>
<body>
<main class="stage">
  <section class="card card--back" aria-label="Verso de la carte">
    <div class="brand">
      <div class="brand__mark"></div>
      <div class="brand__name"><span>Corvane</span><span>Conseil et Registre</span></div>
    </div>
    <div class="web">corvaneconseil.ch</div>
  </section>

  <section class="card card--front" aria-label="Recto de la carte">
    <div class="front__info">
      <div class="brand">
        <div class="brand__name"><span>Corvane</span><span>Conseil et Registre</span></div>
      </div>
      <div class="person">
        <h1 class="person__name">Tomas da Varela</h1>
        <p class="person__role">Directeur et Fondateur<br>Expert-comptable diplômé</p>
      </div>
      <address class="address">Rue des Vergers-Bleus 14<br>1201 Genève</address>
      <ul class="contacts">
        <li>
          <svg viewBox="0 0 24 24" aria-hidden="true"><path d="M6.6 10.8a15.1 15.1 0 0 0 6.6 6.6l2.2-2.2c.3-.3.7-.4 1-.2 1.1.4 2.3.6 3.6.6.6 0 1 .4 1 1V20c0 .6-.4 1-1 1A17 17 0 0 1 3 4c0-.6.4-1 1-1h3.5c.6 0 1 .4 1 1 0 1.3.2 2.5.6 3.6.1.3 0 .7-.2 1z"/></svg>
          022 418 27 35
        </li>
        <li>
          <svg viewBox="0 0 24 24" aria-hidden="true"><path d="M2 5h20v14H2zm2 2v.5l8 5 8-5V7l-8 5z"/></svg>
          tv@corvaneconseil.ch
        </li>
        <li>
          <svg viewBox="0 0 24 24" aria-hidden="true"><circle cx="12" cy="12" r="10"/></svg>
          www.corvaneconseil.ch
        </li>
      </ul>
    </div>
    <div class="front__accent"></div>
  </section>
</main>
</body>
</html>
```